Wavelume artwork for new single release

I need Wavelume artwork creating to release a new single on there.

The specs are:

Ideal size: 3000 x 3000 pixels
Minimum size: 1400 x 1400 pixels
Aspect ratio: 1:1 (must be a perfect square)
File format: JPG or PNG
Color space: sRGB
File size: Max 4MB

The song is called "Still, Can We Wander?"
The artist is "Milo Fenwright"

We have no images of Milo, so it really is open to imagination.

Target Market(s)

Wavelume listeners

Industry/Entity Type

Music

```html
<!DOCTYPE html>
<html lang="en">
<head>
<meta charset="utf-8">
<title>Still, Can We Wander? — Milo Fenwright</title>
<link href="https://fonts.googleapis.com/css2?family=Mr+Dafoe&family=Questrial&display=swap" rel="stylesheet">
<style>
  :root {
    --ink: #222326;
    --paper-edge: #e9e9e9;
    --glow-pink: rgba(233, 133, 131, 0.95);
    --glow-teal: rgba(46, 122, 124, 0.85);
    --glow-blue: rgba(42, 79, 134, 0.85);
    --type: #ffffff;
  }
  html, body {
    margin: 0;
    padding: 0;
    width: 1200px;
    height: 1200px;
    overflow: hidden;
    background: var(--ink);
  }
  .cover {
    position: relative;
    width: 1200px;
    height: 1200px;
    background: var(--ink);
    overflow: hidden;
  }
  .cover__glow {
    position: absolute;
    inset: 0;
    background:
      radial-gradient(ellipse 260px 240px at 590px 500px, var(--glow-pink) 0%, rgba(233,133,131,0.6) 45%, rgba(233,133,131,0) 100%),
      radial-gradient(ellipse 260px 220px at 380px 780px, var(--glow-teal) 0%, rgba(46,122,124,0) 100%),
      radial-gradient(ellipse 280px 240px at 780px 720px, var(--glow-blue) 0%, rgba(42,79,134,0) 100%);
  }
  .cover__frame {
    position: absolute;
    inset: 0;
  }
  .cover__title {
    position: absolute;
    left: 0;
    top: 0;
    width: 1200px;
    height: 1200px;
    margin: 0;
    font-family: "Mr Dafoe", cursive;
    font-weight: 400;
    color: var(--type);
    transform: rotate(-5deg);
    transform-origin: 600px 560px;
  }
  .cover__title-line {
    position: absolute;
    left: 0;
    width: 1200px;
    text-align: center;
    white-space: nowrap;
    line-height: 1;
    font-size: 200px;
  }
  .cover__title-line--first {
    top: 330px;
    padding-right: 60px;
    box-sizing: border-box;
  }
  .cover__title-line--second {
    top: 520px;
    padding-left: 20px;
    box-sizing: border-box;
  }
  .cover__artist {
    position: absolute;
    left: 0;
    width: 1200px;
    top: 1030px;
    margin: 0;
    text-align: center;
    font-family: "Questrial", sans-serif;
    font-size: 44px;
    line-height: 1;
    letter-spacing: 1px;
    color: var(--type);
  }
</style>
</head>
<body>
<main class="cover">
  <div class="cover__glow" role="img" aria-label="Soft glowing light in pink, teal and blue tones"></div>

  <svg class="cover__frame" width="1200" height="1200" viewBox="0 0 1200 1200" aria-hidden="true">
    <rect x="6" y="6" width="1188" height="1188" fill="none" stroke="var(--paper-edge)" stroke-width="5" opacity="0.85"/>
    <line x1="6" y1="93" x2="1194" y2="93" stroke="var(--paper-edge)" stroke-width="1.5" opacity="0.5"/>
    <line x1="0" y1="760" x2="250" y2="1200" stroke="var(--paper-edge)" stroke-width="2" opacity="0.55"/>
    <line x1="1200" y1="920" x2="780" y2="1200" stroke="var(--paper-edge)" stroke-width="2" opacity="0.55"/>
  </svg>

  <h1 class="cover__title">
    <span class="cover__title-line cover__title-line--first">Still, Can</span>
    <span class="cover__title-line cover__title-line--second">We Wander?</span>
  </h1>

  <p class="cover__artist">MILO FENWRIGHT</p>
</main>
</body>
</html>
```